BRC Business cards

We are a medium sized property company based in London and require a logo, Business card which reflects a professional company and incorporates our catchy name.

Our statement is (Building for the future) we like colours such as royal blue, greens and light browns but will look at anything.

Contact Information for Business Card

Brookcrest Estates Limited
Unit 4, 15-17 Farrowby Lane
London
SE22 7QN

Web: www.brookcrestestates-example.com

Email: brookcrestltd@mailbox-example.com

Telephone: +44-208-555-0142
Fax: +44-208-555-0187

```html
<!DOCTYPE html>
<html lang="en">
<head>
<meta charset="utf-8">
<title>Brookcrest Estates Limited – Business Card</title>
<link rel="stylesheet" href="https://fonts.googleapis.com/css2?family=Righteous&display=swap">
<style>
  :root {
    --ink: #000000;
    --lime: #a3f43c;
    --lime-text: #a6f23f;
    --lime-soft: #6fa52a;
    --panel-dark: #0d0d0d;
    --white: #ffffff;
    --badge-ring: #c9c9c9;
    --font-display: "Righteous", sans-serif;
  }
  html, body {
    margin: 0;
    padding: 0;
    width: 791px;
    height: 1200px;
    overflow: hidden;
    background: var(--lime);
  }
  .card {
    position: relative;
    width: 791px;
    height: 1200px;
    font-family: var(--font-display);
    background: var(--lime);
  }
  .brand-panel {
    position: absolute;
    left: 0;
    top: 0;
    width: 791px;
    height: 569px;
    background: var(--ink);
  }
  .brand-artwork {
    position: absolute;
    left: 136px;
    top: 72px;
    width: 494px;
    height: 314px;
    background: linear-gradient(180deg, var(--panel-dark) 0%, var(--lime-soft) 55%, var(--lime) 100%);
  }
  .brand-name {
    position: absolute;
    left: 115px;
    top: 395px;
    margin: 0;
    font-size: 51px;
    font-weight: 400;
    line-height: 1;
    color: var(--lime-text);
    white-space: nowrap;
  }
  .contact-list {
    list-style: none;
    margin: 0;
    padding: 0;
  }
  .contact-item {
    position: absolute;
    left: 26px;
    display: flex;
    align-items: center;
  }
  .contact-badge {
    flex: none;
    width: 68px;
    height: 68px;
    border-radius: 50%;
    background: var(--ink);
    display: flex;
    align-items: center;
    justify-content: center;
  }
  .contact-badge span {
    width: 30px;
    height: 30px;
    border-radius: 50%;
    border: 3px solid var(--badge-ring);
    box-sizing: border-box;
    display: flex;
    align-items: center;
    justify-content: center;
    font-size: 17px;
    line-height: 1;
    color: var(--badge-ring);
  }
  .contact-text {
    margin-left: 22px;
    font-size: 35px;
    line-height: 48px;
    color: var(--white);
    white-space: nowrap;
  }
  .contact-phone .contact-text,
  .contact-fax .contact-text { word-spacing: 6px; }
  .contact-address { top: 646px; align-items: flex-start; }
  .contact-address .contact-badge { margin-top: 12px; }
  .contact-address .contact-text { margin-left: 30px; }
  .contact-phone { top: 761px; }
  .contact-fax { top: 862px; }
  .contact-email { top: 964px; }
  .contact-email .contact-text { font-size: 33px; }
  .contact-web { top: 1056px; }
</style>
</head>
<body>
  <main class="card">
    <header class="brand-panel">
      <div class="brand-artwork" role="img" aria-label="Brand artwork: row of stylised green buildings on black"></div>
      <h1 class="brand-name">Brookcrest Estates Ltd .</h1>
    </header>
    <ul class="contact-list">
      <li class="contact-item contact-address">
        <div class="contact-badge"><span>A</span></div>
        <div class="contact-text">Unit 4, 15-17 Farrowby Lane<br>London, SE22 7QN</div>
      </li>
      <li class="contact-item contact-phone">
        <div class="contact-badge"><span>T</span></div>
        <div class="contact-text">+44&nbsp; 208&nbsp; 555&nbsp; 0142</div>
      </li>
      <li class="contact-item contact-fax">
        <div class="contact-badge"><span>F</span></div>
        <div class="contact-text">+44&nbsp; 208&nbsp; 555&nbsp; 0187</div>
      </li>
      <li class="contact-item contact-email">
        <div class="contact-badge"><span>E</span></div>
        <div class="contact-text">brookcrestltd@mailbox-example.com</div>
      </li>
      <li class="contact-item contact-web">
        <div class="contact-badge"><span>W</span></div>
        <div class="contact-text">brookcrestestates-example.com</div>
      </li>
    </ul>
  </main>
</body>
</html>
```